Facebook & Instagram Ad Design for Chiropractor

I'd like a series of ads developed for our chiropractic office to use on Facebook and Instagram. I've attached the versions we're using today. They need to be updated. The offer content would be generally the same. There are two types of ads we're seeking. One for basic chiropractic services and the other for chiropractic decompression services.

Current ads can be seen in attached and here:
https://lnk.example/8TrQ2zXvPoLkm3A

Learn more about the company at www.bellwingchiropractic.example

Target Market(s)

Potential patients seeking chiropractic care or who are unaware that chiropractic could help them (suffer from back pain, etc.) in the greater Green Bay, WI area.

Industry/Entity Type

Chiropractic

Font styles to use
Sans Serif

Colors
0592cd
3277b5

Requirements
Must have
• Compelling visuals
Comply with text requirements for FB & Insta ads
Should not have
• Clinical images that depict traditional medical care

```html
<!DOCTYPE html>
<html lang="en">
<head>
<meta charset="utf-8">
<title>Bellwing Chiropractic – Ad Set</title>
<link href="https://fonts.googleapis.com/css2?family=Roboto:ital,wght@0,400;0,900;1,400&family=Roboto+Condensed:wght@400;700;800&display=swap" rel="stylesheet">
<style>
  :root{
    --page-bg:#07072a;
    --navy:#1f1a66;
    --red:#ff0a0a;
    --white:#ffffff;
    --brand-blue:#3277b5;
    --brand-cyan:#0592cd;
    --panel-end:#ffffff;
    --highlight:#c9e8f7;
    --skin-light:#e8c4a8;
    --skin-mid:#d9a488;
    --device-light:#f1f3f6;
    --device-mid:#c9ced8;
    --table-blue:#44527c;
  }
  html,body{margin:0;padding:0;overflow:hidden;}
  body{width:1074px;height:1200px;background:var(--page-bg);position:relative;}
  .ad{
    position:absolute;left:48px;width:978px;height:515px;overflow:hidden;
    background:linear-gradient(90deg,var(--brand-blue) 0%,var(--brand-cyan) 38%,#9fd6ee 62%,var(--panel-end) 82%);
  }
  .ad--chiro{top:56px;}
  .ad--decompression{top:628px;}
  .photo{position:absolute;}
  .photo--back-pain{
    left:478px;top:0;width:500px;height:515px;
    background:linear-gradient(180deg,var(--skin-light) 0%,var(--skin-mid) 100%);
  }
  .photo--decompression{
    left:392px;top:180px;width:586px;height:335px;
    background:linear-gradient(180deg,var(--device-light) 0%,var(--device-mid) 60%,var(--table-blue) 100%);
  }
  .shapes{position:absolute;left:0;top:0;width:978px;height:515px;}
  .txt{position:absolute;margin:0;line-height:1;white-space:nowrap;}
  .brand-name{font-family:"Roboto Condensed",sans-serif;font-weight:800;color:var(--navy);}
  .brand-sub{font-family:"Roboto Condensed",sans-serif;font-weight:700;color:var(--red);}
  .offer-line{font-family:"Roboto",sans-serif;font-weight:900;color:var(--white);}
  .price{font-family:"Roboto",sans-serif;font-weight:900;color:var(--navy);letter-spacing:-1px;}
  .price .currency{color:var(--white);}
  .subject-line{font-family:"Roboto",sans-serif;}
  .spinal{font-weight:900;color:var(--red);}
  .decomp{font-family:"Roboto Condensed",sans-serif;font-weight:400;color:var(--navy);}
  .therapy{font-weight:900;color:var(--red);}
  .therapy em{font-weight:400;color:var(--navy);font-style:italic;}
  .city{font-weight:400;color:var(--white);}
  .city strong{font-weight:900;color:var(--red);}
</style>
</head>
<body>

<section class="ad ad--chiro">
  <div class="photo photo--back-pain" role="img" aria-label="Photo area: man holding his lower back in pain"></div>
  <svg class="shapes" viewBox="0 0 978 515" aria-hidden="true">
    <polygon points="0,390 400,390 435,454 0,454" fill="var(--red)"/>
    <polygon points="381,364 566,364 537,482 352,482" fill="none" stroke="var(--navy)" stroke-width="4"/>
  </svg>
  <h1 class="txt brand-name" style="left:44px;top:58px;font-size:96px;">BELLWING</h1>
  <p class="txt brand-sub" style="left:44px;top:146px;font-size:62px;">CHIROPRACTIC</p>
  <p class="txt offer-line" style="left:44px;top:258px;font-size:68px;">NEW</p>
  <p class="txt offer-line" style="left:44px;top:322px;font-size:68px;">PATIENT</p>
  <p class="txt offer-line" style="left:44px;top:389px;font-size:68px;">OFFER</p>
  <p class="txt price" style="left:394px;top:385px;font-size:74px;"><span class="currency">$</span>25</p>
</section>

<section class="ad ad--decompression">
  <div class="photo photo--decompression" role="img" aria-label="Photo area: spinal decompression machine with a patient lying on the treatment table"></div>
  <svg class="shapes" viewBox="0 0 978 515" aria-hidden="true">
    <rect x="50" y="142" width="296" height="40" fill="var(--highlight)"/>
    <polygon points="38,440 300,440 328,483 38,483" fill="var(--red)"/>
    <polygon points="295,435 421,435 402,489 273,489" fill="none" stroke="var(--navy)" stroke-width="3"/>
  </svg>
  <h2 class="txt subject-line spinal" style="left:38px;top:60px;font-size:88px;">SPINAL</h2>
  <p class="txt decomp" style="left:54px;top:143px;font-size:38px;">DECOMPRESSION</p>
  <p class="txt subject-line therapy" style="left:40px;top:182px;font-size:55px;">THERAPY <em>in</em></p>
  <p class="txt subject-line city" style="left:40px;top:233px;font-size:55px;">GREEN <strong>BAY</strong></p>
  <p class="txt brand-name" style="left:624px;top:44px;font-size:80px;">BELLWING</p>
  <p class="txt brand-sub" style="left:624px;top:118px;font-size:50px;">CHIROPRACTIC</p>
  <p class="txt offer-line" style="left:50px;top:390px;font-size:50px;">NEW PATIENT</p>
  <p class="txt offer-line" style="left:50px;top:441px;font-size:46px;">OFFER</p>
  <p class="txt price" style="left:302px;top:442px;font-size:46px;"><span class="currency">$</span>25</p>
</section>

</body>
</html>
```